Valkemo App for Smart Devices IoT WiFi Electronic

Valkemo is a siren manufacturer. This application is used for the company's products that have a Wi-Fi connection and an internet connection, which can be configured and activated remotely through this application. In addition, this application is used to activate the siren at specific times for the start and end of shifts in companies and schools. Users will be siren installers and IT or HR managers.
In addition to activating motorized sirens timers, some siren models have speakers and allow you to play TTS (text to speech) audio, audio recorded by the user on the phone and upload audio (mp3) with playlist programming with start and end times.
Application screens: home with dashboard (one dashboard for each category). Device categories: timers, speakers, motorized siren. Screen for requesting evaluation in the Play Store. Screen for registering the user profile. Screen for registering devices according to their category (timers, speakers, motorized siren). Screen for registering device groups. Screen for pairing the device on the client's Wi-Fi network. Screen for registering activation times. Screen for uploading MP3 audios. Screen for registering playlists with audio selection, start and end times. Screen for recording audio for later sending to the speakers. Screen for converting text to speech and sending to the speakers. It is important to have a time picker with the day of the week to program the activation times and playlist.

Target Market(s)

Schools, Companies and Stores.

Industry/Entity Type

IoT

Font styles to use
Sans Serif
Other font styles liked:
• roboto

Colors
FFC000
F8CF3A
FAE287
FDF2CF
FEFAEE

Requirements
Must have
• time picker with weekdays for timer programming feature.
Nice to have
• app review request screen on play store

```html
<!DOCTYPE html>
<html lang="en">
<head>
<meta charset="UTF-8">
<title>Valkemo – Smart Siren App Screens</title>
<link href="https://fonts.googleapis.com/css2?family=Roboto:wght@400;500;700&display=swap" rel="stylesheet">
<style>
  :root {
    --amber: #FFC000;
    --amber-deep: #F8BF00;
    --amber-soft: #FFD348;
    --ink: #2B1D0A;
    --text: #333333;
    --muted: #9a9a9a;
    --stage: #F1F1F1;
    --screen: #FFFFFF;
    --screen-fill: #F8F8F8;
    --online: #23E79A;
    --field-line: #F2EDDD;
    --shadow: 0 4px 14px rgba(0,0,0,0.05);
  }
  * { box-sizing: border-box; margin: 0; padding: 0; }
  html, body { width: 1200px; height: 900px; overflow: hidden; }
  body {
    background: linear-gradient(180deg, #F5F5F5, #EFEFEF);
    font-family: 'Roboto', sans-serif;
    color: var(--text);
    position: relative;
  }
  .screen {
    position: absolute;
    top: 106px;
    width: 309px;
    height: 688px;
    border-radius: 4px;
    overflow: hidden;
  }
  .screen--splash {
    left: 71px;
    background: linear-gradient(180deg, var(--amber-deep) 0%, var(--amber-deep) 45%, var(--amber-soft) 100%);
    display: flex; align-items: center; justify-content: center;
  }
  .splash-name {
    font-size: 50px; font-weight: 500; color: var(--ink); letter-spacing: 0.5px;
    margin-top: 10px;
  }
  .screen--dashboard { left: 445px; background: var(--screen-fill); }
  .screen--register { left: 820px; background: var(--screen-fill); }

  .app-header {
    position: absolute; left: 0; top: 0; width: 100%; height: 134px;
    background: var(--screen);
  }
  .brand {
    position: absolute; left: 10px; top: 14px;
    font-size: 20px; font-weight: 500; color: var(--amber);
  }
  .icon-button {
    position: absolute; top: 10px; width: 36px; height: 36px; border-radius: 50%;
    background: #F7F7F7; box-shadow: 0 2px 6px rgba(0,0,0,0.06);
    display: flex; align-items: center; justify-content: center;
  }
  .icon-button--bell { left: 219px; }
  .icon-button--profile { left: 264px; }

  .search {
    position: absolute; left: 40px; top: 73px; width: 224px; height: 45px;
    border-radius: 23px; background: #F6F5F5;
    display: flex; align-items: center; justify-content: space-between;
    padding: 0 14px 0 13px; color: #BDBDBD; font-size: 11.5px;
  }

  .section-title {
    position: absolute; left: 27px; top: 148px;
    font-size: 15px; font-weight: 500; color: var(--text);
  }
  .category-card {
    position: absolute; left: 29px; width: 249px; height: 98px;
    background: var(--screen); border-radius: 6px; box-shadow: var(--shadow);
  }
  .category-card__title {
    position: absolute; left: 9px; top: 9px; font-size: 12px; font-weight: 500;
  }
  .status-row {
    position: absolute; left: 9px; display: flex; align-items: center; gap: 4px;
    font-size: 8.5px; color: #444;
  }
  .status-row strong { font-weight: 500; }
  .status-dot {
    width: 14px; height: 14px; border-radius: 50%; background: var(--online);
    display: flex; align-items: center; justify-content: center;
  }
  .status-row--online { top: 47px; }
  .status-row--activated { top: 70px; }
  .expand-link {
    position: absolute; right: 10px; top: 79px; font-size: 8.5px; font-weight: 500; color: #444;
  }

  .add-device-ghost {
    position: absolute; left: 154px; top: 541px; width: 128px; height: 43px;
    background: var(--screen); border-radius: 6px; box-shadow: var(--shadow);
    display: flex; align-items: center; justify-content: center; gap: 8px;
    font-size: 12px; font-weight: 500; color: var(--text);
  }

  .tab-bar {
    position: absolute; left: 44px; top: 626px; width: 220px; height: 44px;
    border-radius: 22px; background: #F6F6F6; box-shadow: 0 3px 10px rgba(0,0,0,0.05);
  }
  .tab-bar svg { position: absolute; top: 11px; }

  .back-button {
    position: absolute; left: 10px; top: 73px; width: 36px; height: 36px; border-radius: 50%;
    background: #F7F7F7; display: flex; align-items: center; justify-content: center;
  }
  .page-title {
    position: absolute; left: 0; width: 100%; top: 83px; padding-left: 0;
    text-align: center; font-size: 15px; font-weight: 500; color: var(--text);
  }
  .form-card {
    position: absolute; left: 35px; top: 149px; width: 239px; height: 405px;
    background: var(--screen); border-radius: 6px; box-shadow: var(--shadow);
  }
  .field-label {
    position: absolute; left: 22px; font-size: 11.5px; font-weight: 500; color: var(--text);
  }
  .field-input {
    position: absolute; left: 22px; width: 194px; height: 38px;
    border: 1px solid var(--field-line); border-radius: 2px; background: #fff;
  }
  .add-device-primary {
    position: absolute; left: 45px; top: 291px; width: 149px; height: 44px;
    background: var(--amber); border-radius: 8px; box-shadow: 0 6px 14px rgba(255,192,0,0.18);
    display: flex; align-items: center; justify-content: center; gap: 9px;
    font-size: 12px; font-weight: 500; color: #3a3a3a;
  }
</style>
</head>
<body>

  <section class="screen screen--splash">
    <span class="splash-name">Valkemo</span>
  </section>

  <section class="screen screen--dashboard">
    <header class="app-header">
      <span class="brand">Valkemo</span>
      <span class="icon-button icon-button--bell">
        <svg width="18" height="20" viewBox="0 0 18 20" fill="none" stroke="#555" stroke-width="1.6" stroke-linecap="round"><path d="M3 14V8a6 6 0 0 1 12 0v6l1.5 2h-15z"/><path d="M7 18.5h4"/></svg>
      </span>
      <span class="icon-button icon-button--profile">
        <svg width="18" height="20" viewBox="0 0 18 20" fill="none" stroke="#555" stroke-width="1.6"><circle cx="9" cy="6" r="4"/><path d="M2 17.5c0-2.5 3-4 7-4s7 1.5 7 4-14 2.5-14 0z"/></svg>
      </span>
      <div class="search">
        <span>Search</span>
        <svg width="18" height="18" viewBox="0 0 18 18" fill="none" stroke="#C9C9C9" stroke-width="1.6" stroke-linecap="round"><circle cx="10" cy="7.5" r="6"/><path d="M5.5 12 2 16"/></svg>
      </div>
    </header>

    <h2 class="section-title">Dashboard</h2>

    <article class="category-card" style="top:187px">
      <h3 class="category-card__title">Timers</h3>
      <div class="status-row status-row--online"><span class="status-dot"></span>Online: <strong>3 Devices</strong></div>
      <div class="status-row status-row--activated"><span class="status-dot"><svg width="8" height="8" viewBox="0 0 8 8" fill="none" stroke="#1a6b45" stroke-width="1.4"><path d="M1 4l2 2 4-4"/></svg></span>Activated: <strong>1 Device</strong></div>
      <span class="expand-link">Expand</span>
    </article>

    <article class="category-card" style="top:307px">
      <h3 class="category-card__title">Speakers</h3>
      <div class="status-row status-row--online"><span class="status-dot"></span>Online: <strong>3 Devices</strong></div>
      <div class="status-row status-row--activated"><span class="status-dot"><svg width="8" height="8" viewBox="0 0 8 8" fill="none" stroke="#1a6b45" stroke-width="1.4"><path d="M1 4l2 2 4-4"/></svg></span>Activated: <strong>2 Devices</strong></div>
    </article>

    <article class="category-card" style="top:427px">
      <h3 class="category-card__title">Motorized Sirens</h3>
      <div class="status-row status-row--online"><span class="status-dot"></span>Online: <strong>2 Devices</strong></div>
      <div class="status-row status-row--activated"><span class="status-dot"><svg width="8" height="8" viewBox="0 0 8 8" fill="none" stroke="#1a6b45" stroke-width="1.4"><path d="M1 4l2 2 4-4"/></svg></span>Activated: <strong>0 Device</strong></div>
    </article>

    <div class="add-device-ghost">
      <svg width="24" height="20" viewBox="0 0 24 20" fill="none" stroke="var(--amber)" stroke-width="1.8" stroke-linecap="round"><path d="M14 15H3a1.5 1.5 0 0 1-1.5-1.5v-10A1.5 1.5 0 0 1 3 2h15a1.5 1.5 0 0 1 1.5 1.5V11"/><path d="M19.5 13v6M16.5 16h6"/></svg>
      Add A Device
    </div>

    <nav class="tab-bar">
      <svg style="left:22px" width="22" height="22" viewBox="0 0 22 22" fill="none" stroke="#555" stroke-width="1.6" stroke-linejoin="round"><path d="M3 9l8-6 8 6v10H3z"/><path d="M9.5 16h3"/></svg>
      <svg style="left:72px" width="24" height="22" viewBox="0 0 24 22" fill="none" stroke="#555" stroke-width="1.6"><rect x="3" y="2" width="7" height="18" rx="1"/><rect x="13" y="8" width="6" height="6"/><path d="M16 2v6M16 14v6M6.5 7v3M6.5 14v2"/></svg>
      <svg style="left:124px" width="22" height="22" viewBox="0 0 22 22" fill="none" stroke="#555" stroke-width="1.6" stroke-linecap="round"><circle cx="11" cy="9" r="7"/><circle cx="11" cy="9" r="3"/><path d="M11 12v9"/></svg>
      <svg style="left:175px" width="22" height="22" viewBox="0 0 22 22" fill="none" stroke="#555" stroke-width="2.4"><circle cx="11" cy="11" r="6.5" stroke-dasharray="3 2.1"/><circle cx="11" cy="11" r="3" stroke-width="1.6"/></svg>
    </nav>
  </section>

  <section class="screen screen--register">
    <header class="app-header">
      <span class="brand">Valkemo</span>
      <span class="icon-button icon-button--bell">
        <svg width="18" height="20" viewBox="0 0 18 20" fill="none" stroke="#555" stroke-width="1.6" stroke-linecap="round"><path d="M3 14V8a6 6 0 0 1 12 0v6l1.5 2h-15z"/><path d="M7 18.5h4"/></svg>
      </span>
      <span class="icon-button icon-button--profile">
        <svg width="18" height="20" viewBox="0 0 18 20" fill="none" stroke="#555" stroke-width="1.6"><circle cx="9" cy="6" r="4"/><path d="M2 17.5c0-2.5 3-4 7-4s7 1.5 7 4-14 2.5-14 0z"/></svg>
      </span>
      <span class="back-button">
        <svg width="22" height="16" viewBox="0 0 22 16" fill="none" stroke="#555" stroke-width="1.8" stroke-linecap="round" stroke-linejoin="round"><path d="M21 8H2M8 2 2 8l6 6"/></svg>
      </span>
      <h1 class="page-title">Register Device</h1>
    </header>

    <form class="form-card">
      <label class="field-label" style="top:53px">Device Name</label>
      <span class="field-input" style="top:74px"></span>
      <label class="field-label" style="top:132px">Category</label>
      <span class="field-input" style="top:152px"></span>
      <label class="field-label" style="top:210px">Device ID</label>
      <span class="field-input" style="top:231px"></span>
      <div class="add-device-primary">
        <svg width="24" height="20" viewBox="0 0 24 20" fill="none" stroke="#3a3a3a" stroke-width="1.8" stroke-linecap="round"><path d="M14 15H3a1.5 1.5 0 0 1-1.5-1.5v-10A1.5 1.5 0 0 1 3 2h15a1.5 1.5 0 0 1 1.5 1.5V11"/><path d="M19.5 13v6M16.5 16h6"/></svg>
        Add A Device
      </div>
    </form>

    <nav class="tab-bar">
      <svg style="left:22px" width="22" height="22" viewBox="0 0 22 22" fill="none" stroke="#555" stroke-width="1.6" stroke-linejoin="round"><path d="M3 9l8-6 8 6v10H3z"/><path d="M9.5 16h3"/></svg>
      <svg style="left:72px" width="24" height="22" viewBox="0 0 24 22" fill="none" stroke="#555" stroke-width="1.6"><rect x="3" y="2" width="7" height="18" rx="1"/><rect x="13" y="8" width="6" height="6"/><path d="M16 2v6M16 14v6M6.5 7v3M6.5 14v2"/></svg>
      <svg style="left:124px" width="22" height="22" viewBox="0 0 22 22" fill="none" stroke="#555" stroke-width="1.6" stroke-linecap="round"><circle cx="11" cy="9" r="7"/><circle cx="11" cy="9" r="3"/><path d="M11 12v9"/></svg>
      <svg style="left:175px" width="22" height="22" viewBox="0 0 22 22" fill="none" stroke="#555" stroke-width="2.4"><circle cx="11" cy="11" r="6.5" stroke-dasharray="3 2.1"/><circle cx="11" cy="11" r="3" stroke-width="1.6"/></svg>
    </nav>
  </section>

</body>
</html>
```